Stonegate Towing Business Card

Towing
Accident towing
Mechanical breakdown
Insurance, salvage and recovery
4wd off road towing
Light & Heavy towing
7354 2618
24 hour business 7 days

Logo can be whole size on front

Industry/Entity Type

Towing/ transport

Contact Information for Business Card

The above

```html
<!DOCTYPE html>
<html lang="en">
<head>
<meta charset="utf-8">
<title>Stonegate Towing Business Card</title>
<link href="https://fonts.googleapis.com/css2?family=Montserrat:wght@400;500;700&display=swap" rel="stylesheet">
<style>
  :root {
    --stage: #a3a3a3;
    --ink: #1a1a1b;
    --red: #d21f2a;
    --paper: #ffffff;
    --text-light: #f4f4f4;
  }
  * { box-sizing: border-box; margin: 0; padding: 0; }
  html, body {
    width: 1200px; height: 1200px; overflow: hidden;
    background: var(--stage);
    font-family: "Montserrat", sans-serif;
  }
  .card {
    position: absolute;
    left: 219px;
    width: 762px;
    height: 422px;
    border-radius: 26px;
    overflow: hidden;
  }
  .card-front {
    top: 161px;
    background: var(--ink);
    display: flex;
    align-items: center;
    justify-content: center;
  }
  .brand-name {
    color: var(--red);
    font-weight: 700;
    white-space: nowrap;
  }
  .card-front .brand-name { font-size: 60px; }
  .card-back { top: 619px; background: var(--paper); }
  .card-back .wave { position: absolute; inset: 0; width: 762px; height: 422px; }
  .card-back .brand-name {
    position: absolute;
    right: 34px;
    top: 74px;
    font-size: 30px;
  }
  .services {
    position: absolute;
    left: 33px;
    top: 164px;
    color: var(--text-light);
  }
  .services-title {
    display: inline-block;
    color: var(--red);
    font-weight: 700;
    font-size: 26px;
    border-bottom: 2px solid var(--red);
    line-height: 1.05;
    margin-bottom: 12px;
  }
  .services-list { list-style: none; }
  .services-list li {
    position: relative;
    padding-left: 16px;
    font-size: 17px;
    line-height: 26.4px;
    letter-spacing: 0.3px;
  }
  .services-list li::before {
    content: "";
    position: absolute;
    left: 0; top: 11px;
    width: 6px; height: 6px;
    border-radius: 50%;
    background: var(--red);
  }
  .contact {
    position: absolute;
    right: 31px;
    top: 296px;
    list-style: none;
    color: var(--text-light);
    text-align: right;
  }
  .contact li {
    display: flex;
    align-items: center;
    justify-content: flex-end;
    gap: 9px;
    font-size: 18px;
    line-height: 30px;
    letter-spacing: 0.3px;
  }
  .contact svg { width: 16px; height: 16px; flex: none; }
</style>
</head>
<body>
  <section class="card card-front">
    <span class="brand-name">Stonegate Towing</span>
  </section>

  <section class="card card-back">
    <svg class="wave" viewBox="0 0 762 422" aria-hidden="true">
      <path fill="#d21f2a" d="M0,128 C140,78 330,110 470,180 C590,238 690,250 762,185 L762,422 L0,422 Z"/>
      <path fill="#ffffff" d="M0,145 C150,100 330,128 470,198 C590,258 690,268 762,210 L762,422 L0,422 Z"/>
      <path fill="#1a1a1b" d="M0,152 C150,110 330,140 470,210 C590,270 690,282 762,230 L762,422 L0,422 Z"/>
    </svg>

    <span class="brand-name">Stonegate Towing</span>

    <div class="services">
      <h2 class="services-title">SERVICES</h2>
      <ul class="services-list">
        <li>Towing</li>
        <li>Accident towing</li>
        <li>Mechanical breakdown</li>
        <li>Insurance, salvage and recovery</li>
        <li>4wd off road towing</li>
        <li>Light &amp; Heavy towing</li>
        <li>24 hour business 7 days</li>
      </ul>
    </div>

    <ul class="contact">
      <li>7354 2618
        <svg viewBox="0 0 16 16" aria-hidden="true"><path fill="#d21f2a" d="M1,6 C1,2 15,2 15,6 L15,7 L11,7 L11,5 L5,5 L5,7 L1,7 Z M4,8 L12,8 L14,14 L2,14 Z"/></svg>
      </li>
      <li>info@stonegatetowing.com
        <svg viewBox="0 0 16 16" aria-hidden="true"><rect x="1" y="3" width="14" height="10" rx="1" fill="#d21f2a"/><path d="M1,4 L8,9 L15,4" fill="none" stroke="#1a1a1b" stroke-width="1.3"/></svg>
      </li>
      <li>www.stonegatetowing.com
        <svg viewBox="0 0 16 16" aria-hidden="true"><circle cx="8" cy="8" r="7" fill="#d21f2a"/><path d="M1,8 H15 M8,1 C4,5 4,11 8,15 M8,1 C12,5 12,11 8,15" fill="none" stroke="#1a1a1b" stroke-width="1"/></svg>
      </li>
    </ul>
  </section>
</body>
</html>
```